Business Card for boutique psychology business

Business card for boutique psychology practice in Melbourne. I want them to be relatively simply with the logo and backing colour taking up the front side. Then, text on the back, with my name; professional title (Clinical Psychologist); website - torvinpsychology.com.au; email: hello@torvinpsychology.com.au; insta: @torvin.psychology.emdr
Back should also have the words: Connect. Integrate. Evolve
Fonts used for logo are: Mikea Demo and Gotham Medium. Use something for back text that will compliment these.
Brand colours uploaded below. I'd like to see options in both olive and blush.

```html
<!DOCTYPE html>
<html lang="en">
<head>
<meta charset="UTF-8">
<title>Torvin Psychology – Business Cards</title>
<link href="https://fonts.googleapis.com/css2?family=Montserrat:wght@300;400;500;600&display=swap" rel="stylesheet">
<style>
  :root {
    --olive: #434a2c;
    --blush: #e8c9b8;
    --white: #ffffff;
    --backdrop: #2b2c30;
  }
  * { margin: 0; padding: 0; box-sizing: border-box; }
  html, body {
    width: 1200px; height: 900px; overflow: hidden;
    background: var(--backdrop);
    font-family: "Montserrat", sans-serif;
  }
  .sheet {
    position: relative; width: 1200px; height: 900px;
    display: flex; align-items: center; justify-content: center; gap: 40px;
  }
  .card {
    position: relative; width: 540px; height: 310px;
    border-radius: 16px; overflow: hidden;
    box-shadow: 0 18px 40px rgba(0,0,0,0.45);
  }
  .card-art { position: absolute; inset: 0; width: 540px; height: 310px; }

  /* info side */
  .holder { position: absolute; left: 26px; top: 40px; color: var(--white); }
  .holder-name { font-weight: 600; font-size: 20px; letter-spacing: 1px; }
  .holder-title { font-weight: 500; font-size: 11.5px; letter-spacing: 0.8px; margin-top: 4px; }
  .contacts { position: absolute; left: 26px; top: 212px; color: var(--olive); font-size: 12.5px; font-weight: 500; }
  .contact-row { display: flex; align-items: center; gap: 10px; margin-bottom: 8px; }
  .contact-row svg { width: 16px; height: 16px; flex: none; }
  .info-brand { position: absolute; right: 30px; top: 78px; text-align: right; color: var(--olive); }
  .brand-name { font-weight: 400; font-size: 54px; letter-spacing: 1px; line-height: 1; }
  .social { position: absolute; right: 26px; bottom: 13px; display: flex; align-items: center; gap: 9px;
    color: var(--white); font-size: 12px; font-weight: 500; letter-spacing: 0.6px; text-transform: uppercase; }
  .social-dot { width: 14px; height: 14px; border: 2px solid var(--white); border-radius: 50%; }

  /* logo side */
  .front-brand { position: absolute; left: 0; right: 0; top: 64px; text-align: center; color: var(--blush); }
  .front-brand .brand-name { font-size: 64px; }
  .tagline { position: absolute; left: 96px; bottom: 18px; color: var(--olive); white-space: nowrap;
    font-size: 15px; font-weight: 300; letter-spacing: 1px;
    transform: rotate(-14deg); transform-origin: left bottom; }
</style>
</head>
<body>
<main class="sheet">

  <section class="card card-info">
    <svg class="card-art" viewBox="0 0 540 310" aria-hidden="true">
      <rect width="540" height="310" fill="var(--olive)"/>
      <path d="M0 180 C140 165 250 80 400 0 L540 0 L540 268 L0 268 Z" fill="var(--white)"/>
      <path d="M0 180 C140 165 250 80 400 0 L428 0 C270 90 160 185 0 205 Z" fill="var(--blush)"/>
      <path d="M250 100 C300 60 360 25 440 0 L447 0 C370 28 310 62 257 102 Z" fill="var(--blush)"/>
    </svg>
    <div class="holder">
      <p class="holder-name">TORVIN</p>
      <p class="holder-title">CLINICAL PSYCHOLOGIST</p>
    </div>
    <div class="contacts">
      <p class="contact-row">
        <svg viewBox="0 0 16 16"><rect x="1" y="3" width="14" height="10" fill="none" stroke="var(--blush)" stroke-width="1.6"/><path d="M1 3 L8 9 L15 3" fill="none" stroke="var(--blush)" stroke-width="1.6"/></svg>
        hello@torvinpsychology.com.au
      </p>
      <p class="contact-row">
        <svg viewBox="0 0 16 16"><circle cx="8" cy="8" r="6.5" fill="none" stroke="var(--blush)" stroke-width="1.5"/><ellipse cx="8" cy="8" rx="3" ry="6.5" fill="none" stroke="var(--blush)" stroke-width="1.2"/><path d="M1.5 8 H14.5" stroke="var(--blush)" stroke-width="1.2"/></svg>
        torvinpsychology.com.au
      </p>
    </div>
    <div class="info-brand">
      <p class="brand-name">torvin</p>
    </div>
    <div class="social">
      <span class="social-dot"></span>
      <span>@torvin.psychology.emdr</span>
    </div>
  </section>

  <section class="card card-logo">
    <svg class="card-art" viewBox="0 0 540 310" aria-hidden="true">
      <rect width="540" height="310" fill="var(--olive)"/>
      <path d="M0 232 C200 215 380 150 540 70 L540 310 L0 310 Z" fill="var(--blush)"/>
      <path d="M0 262 C200 218 380 152 540 82" fill="none" stroke="var(--olive)" stroke-width="3"/>
      <path d="M230 198 C360 160 460 115 540 60" fill="none" stroke="var(--blush)" stroke-width="1.5"/>
    </svg>
    <div class="front-brand">
      <p class="brand-name">torvin</p>
    </div>
    <p class="tagline">Connect • Integrate • Evolve</p>
  </section>

</main>
</body>
</html>
```